Business Card Design - Photographer

I am a landscape photographer and I require a business card design. 

I require two designs:
1)  a double sided business card
 and
b)  a single sided business card 

The single sided design can either be the same as the double sided (with just one side having all the information)....or it can be an entire new design. Its up to you.

My corporate colours are (CMYK):

Blue   69, 32, 0, 0
Grey  72,  64,  47,  31
Green  32,  2,  91,  0
Yellow   0, 19, 92, 0
Orange  0, 39, 75, 0

Colour space in final file should be in CMYK.

The details that need to be included on the card:

- Use the provided Logo
- Name: Lukas Wendrovski
- Email:   sales@vistaplume.com.au
- Website:    vistaplume.com.au
- Twitter:    twitter.com/vistaplume
- Facebook:   facebook.com/vistaplume
- Mobile  0415 309 662

Please use the attached template to design the logo to the specified size, including the marked bleed lines. I have also attached my logo in PNG (transparent background) and ai format for you to use.

The final file should be:
- Photoshop version with layers so I can edit the name/text etc. All non vector files should be high resolution at 1039 x 697 pixels at 300 dpi.

I also require a file as:
- Vector based PDF

Anyway questions please contact me.

Thank you

Industry/Entity Type

Landscape

Logo styles of interest
Pictorial/Combination Logo
Abstract Logo
Wordmark Logo
Lettermark Logo
Requirements
Must have
• The details that need to be included on the card:

- Use the provided Logo
- Name: Lukas Wendrovski
- Email: sales@vistaplume.com.au
- Website: vistaplume.com.au
- Twitter: twitter.com/vistaplume
- Facebook: facebook.com/vistaplume
- Mobile 0415 309 662

```html
<!DOCTYPE html>
<html lang="en">
<head>
<meta charset="utf-8">
<title>Vista Plume – Business Card</title>
<link rel="stylesheet" href="https://fonts.googleapis.com/css2?family=Cinzel:wght@400&family=Questrial&display=swap">
<style>
  :root {
    --backdrop: #b9bcbc;
    --card-front: #3b3a4a;
    --card-back: #f2f1ef;
    --ink-light: #eeeef0;
    --ink-dark: #4a4a4f;
    --rule: #55555a;
    --accent-blue: #4f9ad8;
  }
  * { margin: 0; padding: 0; box-sizing: border-box; }
  html, body { width: 1200px; height: 900px; overflow: hidden; }
  body {
    background: var(--backdrop);
    display: flex;
    align-items: center;
    justify-content: center;
    gap: 60px;
  }
  .card {
    width: 510px;
    height: 342px;
    position: relative;
    box-shadow: 0 6px 18px rgba(0,0,0,0.18);
  }
  .card--front {
    background: var(--card-front);
    display: flex;
    align-items: center;
    justify-content: center;
  }
  .brand {
    display: flex;
    flex-direction: column;
    align-items: center;
    color: var(--ink-light);
  }
  .brand__row {
    display: flex;
    align-items: center;
    gap: 14px;
  }
  .brand__dot {
    width: 34px;
    height: 34px;
    border-radius: 50%;
    background: var(--ink-light);
  }
  .brand__name {
    font-family: "Cinzel", serif;
    font-size: 30px;
    letter-spacing: 2px;
    line-height: 1;
  }
  .brand__rule {
    width: 230px;
    height: 1px;
    background: var(--ink-light);
    margin: 10px 0 7px;
  }
  .brand__tagline {
    font-family: "Cinzel", serif;
    font-size: 10px;
    letter-spacing: 3px;
  }
  .card--back {
    background: var(--card-back);
    color: var(--ink-dark);
    font-family: "Questrial", sans-serif;
  }
  .contact {
    position: absolute;
    left: 40px;
    bottom: 44px;
    width: 330px;
  }
  .contact__name {
    font-size: 22px;
    letter-spacing: 1px;
    text-transform: uppercase;
    padding-bottom: 8px;
    border-bottom: 1px solid var(--rule);
    width: 260px;
  }
  .contact__list {
    margin-top: 12px;
    display: grid;
    grid-template-columns: 84px 1fr;
    row-gap: 3px;
    font-size: 12px;
    padding-bottom: 12px;
    border-bottom: 1px solid var(--rule);
  }
  .contact__list dt { color: var(--ink-dark); }
  .contact__list dd::before { content: ": "; }
</style>
</head>
<body>
  <section class="card card--front" aria-label="Business card front">
    <div class="brand">
      <div class="brand__row">
        <span class="brand__dot" aria-hidden="true"></span>
        <span class="brand__name">Vista Plume</span>
      </div>
      <span class="brand__rule" aria-hidden="true"></span>
      <span class="brand__tagline">FINE ART PHOTOGRAPHY</span>
    </div>
  </section>

  <section class="card card--back" aria-label="Business card back">
    <div class="contact">
      <h1 class="contact__name">Lukas Wendrovski</h1>
      <dl class="contact__list">
        <dt>Mobile</dt><dd>0415 309 662</dd>
        <dt>E-mail</dt><dd>sales@vistaplume.com.au</dd>
        <dt>Twitter</dt><dd>twitter.com/vistaplume</dd>
        <dt>Facebook</dt><dd>facebook.com/vistaplume</dd>
        <dt>Web</dt><dd>vistaplume.com.au</dd>
      </dl>
    </div>
  </section>
</body>
</html>
```